5 CD Designs for 5 albums soon on tunevault and brindle music

I'm looking for something fairly unique, i make music shameless plug: www.wavecrate.net/tidalmoth and i'm looking for 5 EP covers. 4 of my EP's are allready listed called:

Glass & Ember
Reed & Salt
Hollow & Frost

and i'm working on a new one in the next month.

I'm looking for a unique design style that matches the music but also something that carries that same style across the 5 designs.

Now i know exposure doesn't pay the bills but i promise to give credit as much as i can, i'm also looking for someone who could keep providing artwork for the albums of the future

Font styles to use
Decorative
Script

Colors
ffffff
85cae6
0692cd

Requirements
Must have
• 5 unique designs
Nice to have
• a nominalistic representation of the music

```html
<!DOCTYPE html>
<html lang="en">
<head>
<meta charset="utf-8">
<title>tidalmoth — EP cover variants</title>
<link href="https://fonts.googleapis.com/css2?family=Kaushan+Script&display=swap" rel="stylesheet">
<style>
  :root {
    --stage: #141618;
    --cover-edge: #0b0b0d;
    --rose-deep: #2a1022;
    --rose-mid: #7a3d63;
    --rose-light: #d9a9c4;
    --rose-mark: #e0297f;
    --ember-deep: #2b0e10;
    --ember-mid: #a0332c;
    --ember-light: #e8a39a;
    --ember-mark: #4fb324;
    --steel-light: #e9e2ee;
    --steel-mid: #8c6f95;
    --steel-dark: #2c2232;
  }
  * { margin: 0; padding: 0; box-sizing: border-box; }
  html, body {
    width: 1200px;
    height: 1200px;
    overflow: hidden;
    background: var(--stage);
  }
  .cover-sheet {
    width: 1200px;
    height: 1200px;
    display: flex;
    flex-direction: column;
    align-items: center;
    justify-content: center;
    gap: 50px;
  }
  .cover {
    position: relative;
    width: 525px;
    height: 525px;
    border-radius: 4px;
    overflow: hidden;
    border: 1px solid var(--cover-edge);
    box-shadow: 0 10px 30px rgba(0, 0, 0, 0.6);
  }
  .cover-artwork {
    position: absolute;
    inset: 0;
  }
  .cover--rose .cover-artwork {
    background:
      radial-gradient(circle at 83% 40%, var(--steel-light) 0 9%, var(--steel-mid) 13%, var(--steel-dark) 16%, transparent 17.5%),
      radial-gradient(ellipse at 75% 95%, var(--rose-light) 0%, var(--rose-mid) 45%, transparent 75%),
      radial-gradient(ellipse at 100% 0%, var(--rose-mid) 0%, var(--rose-deep) 60%),
      var(--rose-deep);
  }
  .cover--ember .cover-artwork {
    background:
      radial-gradient(circle at 83% 40%, var(--steel-light) 0 9%, var(--steel-mid) 13%, var(--steel-dark) 16%, transparent 17.5%),
      radial-gradient(ellipse at 75% 95%, var(--ember-light) 0%, var(--ember-mid) 45%, transparent 75%),
      radial-gradient(ellipse at 100% 0%, var(--ember-mid) 0%, var(--ember-deep) 60%),
      var(--ember-deep);
  }
  .cover-artwork::before {
    content: "";
    position: absolute;
    left: -40%;
    top: -10%;
    width: 60%;
    height: 120%;
    border-radius: 50%;
    background: rgba(10, 6, 14, 0.75);
  }
  .artist-name {
    position: absolute;
    left: 70px;
    top: 200px;
    font-family: "Kaushan Script", cursive;
    font-size: 62px;
    line-height: 1;
  }
  .cover--rose .artist-name { color: var(--rose-mark); }
  .cover--ember .artist-name { color: var(--ember-mark); }
</style>
</head>
<body>
  <main class="cover-sheet">
    <section class="cover cover--rose">
      <div class="cover-artwork" role="img" aria-label="Close-up photograph of a woven speaker cone with a polished metal dust cap, in rose and violet tones"></div>
      <span class="artist-name">tidalmoth</span>
    </section>
    <section class="cover cover--ember">
      <div class="cover-artwork" role="img" aria-label="Close-up photograph of a woven speaker cone with a polished metal dust cap, in red and ember tones"></div>
      <span class="artist-name">tidalmoth</span>
    </section>
  </main>
</body>
</html>
```